Corvant Systems Business Card

Create an appealing and elegant Business card for corvant systems. Include logo and use related colors from website, be creative. Include Business name, my name, tile, address, contacts, address, and social media contacts if possible. Logo PSD file is attached.

Bleed Area: 3.46" x 2.32"
Trim: 3.3" x 2.16"
Safe Area: 3.14" x 2.02"

Save files as vector-based PDF with outlined text and PNG.
No crop marks
CMYK color setting

Business Card Info:

Corvant Systems

Dennis Halvorsen
Owner

512 Brindlemoor Rd Unit C
Marrowfield Bay 02871
t. 1.888.555.0162
e. dennis.h@corvantsys.example
w. www.corvantsys.example

facebook. www.facebook.com/CorvantSys
twitter. twitter.com/corvantsys
pinterest. www.pinterest.com/corvantsys/

Target Market(s)

Business Owners and Partners

Industry/Entity Type

Business

Requirements
Must have
• Logo and related colors from website

```html
<!DOCTYPE html>
<html lang="en">
<head>
<meta charset="utf-8">
<title>Corvant Systems Business Card</title>
<link rel="stylesheet" href="https://fonts.googleapis.com/css2?family=Open+Sans:wght@400;600;700&display=swap">
<style>
  :root {
    --stage: #2f3033;
    --paper: #ffffff;
    --brand-blue: #4a73a8;
    --ink: #141414;
    --ink-soft: #3a3a3a;
    --on-blue: #ffffff;
  }
  * { box-sizing: border-box; margin: 0; padding: 0; }
  html, body {
    width: 1200px; height: 780px; overflow: hidden;
    background: var(--stage);
    font-family: "Open Sans", Arial, sans-serif;
  }
  .canvas { position: relative; width: 1200px; height: 780px; }

  .card {
    position: absolute; top: 215px;
    width: 540px; height: 350px;
    background: var(--paper);
    overflow: hidden;
    box-shadow: 0 14px 30px rgba(0,0,0,.45);
  }
  .card--front { left: 30px; }
  .card--back  { left: 630px; }

  /* Front */
  .front-wave { position: absolute; inset: 0; }
  .front-wave .wave-blue { fill: var(--brand-blue); }
  .front-wave .wave-black { fill: var(--ink); }
  .wordmark {
    position: absolute; left: 46px; top: 108px;
    color: var(--ink); font-weight: 600; line-height: 1;
  }
  .wordmark__line { display: block; font-size: 50px; letter-spacing: .5px; white-space: nowrap; }
  .wordmark__line + .wordmark__line { margin-top: 6px; }

  /* Back */
  .back-top { position: absolute; left: 0; top: 0; width: 100%; height: 138px; background: var(--paper); }
  .back-strip {
    position: absolute; left: 0; top: 138px; width: 100%; height: 34px;
    background: var(--ink); color: var(--on-blue);
    display: flex; align-items: center; gap: 8px;
    padding-left: 28px; font-size: 13px; letter-spacing: .2px;
    white-space: nowrap;
  }
  .back-panel { position: absolute; left: 0; top: 172px; width: 100%; height: 178px; background: var(--brand-blue); color: var(--on-blue); }

  .wordmark--small { left: 28px; top: 30px; }
  .wordmark--small .wordmark__line { font-size: 30px; letter-spacing: .3px; }
  .wordmark--small .wordmark__line + .wordmark__line { margin-top: 3px; }

  .holder { position: absolute; right: 30px; top: 72px; text-align: right; }
  .holder__name { font-size: 22px; color: var(--ink); font-weight: 400; white-space: nowrap; }
  .holder__first { color: var(--brand-blue); font-weight: 700; }
  .holder__title { font-size: 13px; color: var(--ink-soft); margin-top: 2px; margin-right: 48px; }

  .contact-list { position: absolute; top: 26px; list-style: none; font-size: 13px; }
  .contact-list--main { left: 28px; }
  .contact-list--social { left: 300px; top: 78px; }
  .contact-list li { display: flex; align-items: center; gap: 9px; height: 22px; white-space: nowrap; }
  .icon { width: 12px; height: 12px; flex: none; }
  .icon * { fill: var(--on-blue); }
  .icon--dot { width: 8px; height: 8px; border-radius: 50%; background: var(--on-blue); margin: 0 2px; flex: none; }
</style>
</head>
<body>
<main class="canvas">

  <section class="card card--front" aria-label="Card front">
    <svg class="front-wave" viewBox="0 0 540 350" aria-hidden="true">
      <path class="wave-blue" d="M300 0 H540 V350 H150 C290 305 362 225 362 140 C362 80 342 32 300 0 Z"/>
      <path class="wave-black" d="M150 350 C268 318 338 262 356 188 C354 268 306 326 232 350 Z"/>
    </svg>
    <div class="wordmark">
      <span class="wordmark__line">Corvant</span>
      <span class="wordmark__line">Systems</span>
    </div>
  </section>

  <section class="card card--back" aria-label="Card back">
    <div class="back-top">
      <div class="wordmark wordmark--small">
        <span class="wordmark__line">Corvant</span>
        <span class="wordmark__line">Systems</span>
      </div>
      <div class="holder">
        <p class="holder__name"><span class="holder__first">Dennis</span> Halvorsen</p>
        <p class="holder__title">Owner</p>
      </div>
    </div>

    <div class="back-strip">
      <svg class="icon" viewBox="0 0 12 12" aria-hidden="true"><path d="M6 0a4 4 0 0 0-4 4c0 3 4 8 4 8s4-5 4-8a4 4 0 0 0-4-4zm0 5.6A1.6 1.6 0 1 1 6 2.4a1.6 1.6 0 0 1 0 3.2z"/></svg>
      <span>512 Brindlemoor Rd Unit C, Marrowfield Bay 02871</span>
    </div>

    <div class="back-panel">
      <ul class="contact-list contact-list--main">
        <li>
          <svg class="icon" viewBox="0 0 12 12" aria-hidden="true"><path d="M2.4 0.6l2 2-1 1.4c.7 1.6 2 2.9 3.6 3.6l1.4-1 2 2-1.2 1.8C5 10 1.9 6.9 0.6 1.8z"/></svg>
          <span>1.888.555.0162</span>
        </li>
        <li>
          <svg class="icon" viewBox="0 0 12 12" aria-hidden="true"><path d="M6 0a6 6 0 1 0 3 11.2l-.6-1A4.8 4.8 0 1 1 10.8 6v.6c0 .6-.4 1-.9 1s-.9-.4-.9-1V3.4H7.9v.5A3 3 0 1 0 8.3 8a2.1 2.1 0 0 0 3.7-1.4V6A6 6 0 0 0 6 0zm0 7.8A1.8 1.8 0 1 1 6 4.2a1.8 1.8 0 0 1 0 3.6z"/></svg>
          <span>dennis.h@corvantsys.example</span>
        </li>
        <li>
          <svg class="icon" viewBox="0 0 12 12" aria-hidden="true"><path d="M6 0a6 6 0 1 0 0 12A6 6 0 0 0 6 0zm4.7 5.4H8.6A9 9 0 0 0 7.7 1.6a4.8 4.8 0 0 1 3 3.8zM6 1.3c.6.9 1.3 2.3 1.4 4.1H4.6C4.7 3.6 5.4 2.2 6 1.3zM4.3 1.6a9 9 0 0 0-.9 3.8H1.3a4.8 4.8 0 0 1 3-3.8zM1.3 6.6h2.1a9 9 0 0 0 .9 3.8 4.8 4.8 0 0 1-3-3.8zM6 10.7c-.6-.9-1.3-2.3-1.4-4.1h2.8c-.1 1.8-.8 3.2-1.4 4.1zm1.7-.3a9 9 0 0 0 .9-3.8h2.1a4.8 4.8 0 0 1-3 3.8z"/></svg>
          <span>www.corvantsys.example</span>
        </li>
      </ul>

      <ul class="contact-list contact-list--social">
        <li><span class="icon--dot" aria-hidden="true"></span><span>/CorvantSys</span></li>
        <li><span class="icon--dot" aria-hidden="true"></span><span>/corvantsys</span></li>
        <li><span class="icon--dot" aria-hidden="true"></span><span>/corvantsys</span></li>
      </ul>
    </div>
  </section>

</main>
</body>
</html>
```